Marine Business Card

We install Lighting, Sound, Video, PA Systems to hotels, nightclubs, Restaurants, Cruise Ships.

Target Market(s)

We want to focus on the Marine or Maritime/Cruise industry. Passenger ships and cruise liners are the companies we want to appeal to

Industry/Entity Type

Business

Contact Information for Business Card

Mark Dellow
Managing Director
Harbourne Beam and Audio Marine Ltd

Requirements
Must have
• Office: 01632 960418
Mobile: 07700 900371
mark@harbournebeamandaudio.co.uk
www.harbournebeamandaudio.co.uk

```html
<!DOCTYPE html>
<html lang="en">
<head>
<meta charset="utf-8">
<title>Harbourne Beam and Audio Marine Ltd – Business Card</title>
<link rel="stylesheet" href="https://fonts.googleapis.com/css2?family=Michroma&family=Open+Sans:wght@400;700&family=Roboto+Condensed:wght@700&family=Exo+2:wght@300&display=swap">
<style>
  :root {
    --page: #ffffff;
    --card-white: #ffffff;
    --ink: #111111;
    --strip-black: #050505;
    --strip-grey: #1e1e1e;
    --space-deep: #050b16;
    --space-blue: #0f2a4a;
    --sea-blue: #1f5e96;
    --logo-white: #f4f6f8;
  }
  html, body {
    margin: 0;
    width: 1200px;
    height: 1000px;
    overflow: hidden;
    background: var(--page);
  }
  .canvas {
    position: relative;
    width: 1200px;
    height: 1000px;
  }
  .card {
    position: absolute;
    left: 264px;
    width: 657px;
    height: 434px;
    overflow: hidden;
    box-shadow: 0 10px 22px rgba(0,0,0,0.35);
  }

  /* Front: contact side */
  .card--contact {
    top: 46px;
    background: var(--card-white);
  }
  .brand-strip {
    position: absolute;
    left: 0; top: 0;
    width: 154px; height: 434px;
    background: linear-gradient(90deg, var(--strip-black) 0%, var(--strip-grey) 55%, var(--strip-black) 100%);
  }
  .brand-strip__name {
    position: absolute;
    left: 66px; top: 228px;
    transform: translate(-50%, -50%) rotate(90deg);
    text-align: center;
    white-space: nowrap;
    color: var(--logo-white);
    font-family: "Exo 2", sans-serif;
    font-weight: 300;
  }
  .brand-strip__word { font-size: 46px; line-height: 1; display: block; }
  .brand-strip__sub { font-size: 10px; letter-spacing: 0.5px; display: block; margin-top: 2px; }

  .person {
    position: absolute;
    right: 29px; top: 18px;
    text-align: right;
  }
  .person__name {
    font-family: "Michroma", sans-serif;
    font-size: 40px;
    letter-spacing: 3px;
    color: var(--ink);
    text-shadow: 3px 4px 4px rgba(0,0,0,0.45);
    line-height: 1.2;
  }
  .person__role {
    font-family: "Open Sans", sans-serif;
    font-weight: 700;
    font-size: 24px;
    color: var(--ink);
    line-height: 1.15;
  }
  .services {
    position: absolute;
    left: 160px; right: 16px; top: 126px;
    margin: 0;
    text-align: center;
    font-family: "Roboto Condensed", sans-serif;
    font-weight: 700;
    font-size: 23px;
    line-height: 29px;
    color: var(--ink);
  }
  .details {
    position: absolute;
    left: 170px; top: 212px;
    font-family: "Open Sans", sans-serif;
    color: var(--ink);
    font-size: 24px;
    line-height: 33px;
    letter-spacing: 1.2px;
  }
  .details p { margin: 0; }
  .details .details__web { font-size: 21px; letter-spacing: 1.3px; line-height: 32px; }

  /* Back: brand side */
  .card--brand {
    top: 520px;
  }
  .brand-scene {
    position: absolute; inset: 0;
    background: linear-gradient(180deg, var(--space-deep) 0%, var(--space-blue) 55%, var(--sea-blue) 100%);
  }
  .brand-lockup {
    position: absolute;
    left: 0; right: 0; top: 104px;
    text-align: center;
    color: var(--logo-white);
    font-family: "Exo 2", sans-serif;
    font-weight: 300;
  }
  .brand-lockup__word { font-size: 96px; line-height: 1; display: block; letter-spacing: 2px; }
  .brand-lockup__sub { font-size: 31px; letter-spacing: 1px; display: block; margin-top: 8px; }
</style>
</head>
<body>
<main class="canvas">
  <section class="card card--contact">
    <div class="brand-strip" role="img" aria-label="Black side panel with decorative white swirl artwork"></div>
    <div class="brand-strip__name">
      <span class="brand-strip__word">harbourne</span>
      <span class="brand-strip__sub">Beam and Audio Marine Ltd.</span>
    </div>

    <header class="person">
      <div class="person__name">Mark Dellow</div>
      <div class="person__role">Managing Director</div>
    </header>

    <p class="services">Design, Supply, Service &amp; Installation of<br>Lighting and Sound throughout the UK and Europe</p>

    <div class="details">
      <p>14 - 16 Quay Road, Fleetmoor,</p>
      <p>Lancashire, UK, FM4 2QT</p>
      <p>Office: 01632 960418</p>
      <p>Mobile: 07700 900371</p>
      <p class="details__web">mark@harbournebeamandaudio.co.uk</p>
      <p class="details__web">www.harbournebeamandaudio.co.uk</p>
    </div>
  </section>

  <section class="card card--brand">
    <div class="brand-scene" role="img" aria-label="Photograph of a night sky over the sea"></div>
    <div class="brand-lockup">
      <span class="brand-lockup__word">harbourne</span>
      <span class="brand-lockup__sub">Beam and Audio Marine Ltd.</span>
    </div>
  </section>
</main>
</body>
</html>
```